Road Construction Company needs business cards

We would like a new business card designed for our business.

We're a road construction company based in Qld, Australia.

Can the business card please have the following information on it.

Name: Brent Malvoy
Position: General Manager
Phone: 0471 592 304
Email: Brent.malvoy@quendix.com.au
Address: 87 Harrowgate Ave, Pindarra, QLD, 4000
Website: www.quendix.com.au

Visually we'd like the card to be professional and simple.

Attached is our logo.

Our website is www.quendix.com.au

Target Market(s)

Men aged 25-60

Contact Information for Business Card

As listed in project description

Font styles to use
Serif

Requirements
Must have
• Large logo on back of card

```html
<!DOCTYPE html>
<html lang="en">
<head>
<meta charset="utf-8">
<title>Quendix Business Card</title>
<link rel="stylesheet" href="https://fonts.googleapis.com/css2?family=Poppins:wght@300;400;700&display=swap">
<style>
  :root {
    --stage: #444444;
    --brand-blue: #0d4fa3;
    --brand-blue-deep: #0a4596;
    --accent-blue: #3a9ad9;
    --ink: #3a3a3a;
    --paper: #ffffff;
    --facet: #eeeeee;
  }
  * { margin: 0; padding: 0; box-sizing: border-box; }
  html, body { width: 1200px; height: 801px; overflow: hidden; }
  body {
    background: var(--stage);
    font-family: "Poppins", sans-serif;
    position: relative;
  }
  .card {
    position: absolute;
    top: 252px;
    width: 520px;
    height: 297px;
    overflow: hidden;
  }
  .card-front { left: 60px; background: var(--paper); }
  .card-back {
    left: 620px;
    background: linear-gradient(135deg, var(--brand-blue-deep) 0%, #1659ad 60%, #2c70bd 100%);
  }
  .facets { position: absolute; inset: 0; }
  .front-logo {
    position: absolute;
    left: 44px; top: 112px;
    display: flex; align-items: center; gap: 8px;
    color: var(--brand-blue);
    font-weight: 700;
    font-size: 30px;
    letter-spacing: 1px;
  }
  .logo-mark { width: 12px; height: 12px; background: var(--accent-blue); }
  .rule {
    width: 28px; height: 2px; background: var(--accent-blue);
    position: absolute;
  }
  .address-rule { left: 44px; top: 186px; }
  .address {
    position: absolute; left: 44px; top: 196px;
    font-size: 12px; line-height: 18px; color: var(--ink);
  }
  .person { position: absolute; left: 276px; top: 72px; }
  .person-name {
    color: var(--brand-blue); font-weight: 700; font-size: 24px; line-height: 30px;
  }
  .person-title {
    color: var(--accent-blue); font-weight: 300; font-size: 16px; line-height: 22px;
  }
  .person-rule { left: 0; top: 62px; }
  .contacts {
    position: absolute; left: 276px; top: 150px; list-style: none;
    font-size: 11.5px; line-height: 20px; color: var(--ink);
  }
  .contacts li { display: flex; align-items: center; gap: 8px; }
  .contacts svg { width: 11px; height: 11px; fill: var(--brand-blue); flex: none; }
  .back-logo {
    position: absolute; inset: 0;
    display: flex; align-items: center; justify-content: center; gap: 14px;
    color: #ffffff; font-weight: 700; font-size: 62px; letter-spacing: 3px;
  }
  .back-logo .logo-mark { width: 22px; height: 22px; }
</style>
</head>
<body>
  <section class="card card-front">
    <svg class="facets" viewBox="0 0 520 297" aria-hidden="true">
      <polygon points="250,0 520,0 520,40" fill="#f3f3f3"/>
      <polygon points="250,0 520,40 330,297" fill="#f6f6f6"/>
      <polygon points="250,0 330,297 230,297" fill="#fafafa"/>
    </svg>
    <div class="front-logo"><span class="logo-name">QUENDIX</span><span class="logo-mark"></span></div>
    <span class="rule address-rule"></span>
    <p class="address">87 Harrowgate Ave,<br>Pindarra, QLD, 4000</p>
    <div class="person">
      <h1 class="person-name">Brent Malvoy</h1>
      <p class="person-title">General Manager</p>
      <span class="rule person-rule"></span>
    </div>
    <ul class="contacts">
      <li><svg viewBox="0 0 24 24"><path d="M6.6 10.8a15.1 15.1 0 0 0 6.6 6.6l2.2-2.2c.3-.3.7-.4 1-.2 1.1.4 2.3.6 3.6.6.6 0 1 .4 1 1V20c0 .6-.4 1-1 1A17 17 0 0 1 3 4c0-.6.4-1 1-1h3.5c.6 0 1 .4 1 1 0 1.3.2 2.5.6 3.6.1.3 0 .7-.2 1z"/></svg>0471 592 304</li>
      <li><svg viewBox="0 0 24 24"><path d="M2 5h20v14H2zm2 2v.5l8 5 8-5V7z"/></svg>Brent.malvoy@quendix.com.au</li>
      <li><svg viewBox="0 0 24 24"><circle cx="12" cy="12" r="10"/></svg>www.quendix.com.au</li>
    </ul>
  </section>

  <section class="card card-back">
    <svg class="facets" viewBox="0 0 520 297" aria-hidden="true">
      <polygon points="300,0 520,297 420,297" fill="#ffffff" fill-opacity="0.05"/>
      <polygon points="200,0 300,0 250,297 140,297" fill="#ffffff" fill-opacity="0.04"/>
      <polygon points="300,0 520,200 520,297" fill="#ffffff" fill-opacity="0.06"/>
    </svg>
    <div class="back-logo"><span class="logo-name">QUENDIX</span><span class="logo-mark"></span></div>
  </section>
</body>
</html>
```